Half Wrap Design for Dual Cab Marendo Kestra LX 4x4– TAV Surveyors Fleet Branding

Project Description:
TAV Surveyors is looking for a skilled graphic designer to create a half-wrap vehicle design for our fleet of Marendo Kestra LX 4x4 dual cab vehicles. The design should reflect our brand identity and be consistent with the visual style found on our website: https://tavsurveyors-example.com.au.
Design Requirements:
• Half-wrap only: The design should cover the rear half of the vehicle, including both sides and the tailgate. The front half of the vehicle will remain unwrapped.
• Lid design: Include a top-down design element on the tray lid that is visible from aerial views (e.g., drone photography). This could be a logo, pattern, or bold branding element.
• Design must be clean, professional, and modern, suitable for a surveying company operating across construction and infrastructure projects.
• Incorporate TAV Surveyors’ logo, colour palette, and typography as seen on our brand guidelines.
• Include our website URL and optionally a tagline such as “The Land Measurement & 3D Site Scanning Experts.”
• Design should be eye-catching but not overly busy—clarity and legibility are key.
Vehicle Details:
• Model: Marendo Kestra LX 4x4 Dual Cab (2023/2024)
• Consider wrap constraints such as door handles, windows, curves, and tray lid contours.
Deliverables:
• Final wrap design files in vector format (AI, EPS, or PDF)
• Mock-ups showing the design on the vehicle from multiple angles (side, rear, top)
• Colour codes and font specifications
• Notes for installation and layout guidance
Inspiration:
Visit https://tavsurveyors-example.com.au to understand our brand style. We want the vehicle to feel like a mobile extension of our website and corporate identity.
Audience:
Our fleet is seen daily by clients, contractors, and the public on construction sites and urban roads. The design should reinforce our reputation for precision, reliability, and professionalism.

```html
<!DOCTYPE html>
<html lang="en">
<head>
<meta charset="utf-8">
<title>TAV Surveyors – Kestra LX Half Wrap Layout</title>
<link rel="stylesheet" href="https://fonts.googleapis.com/css2?family=Archivo:wght@400;600;800&display=swap">
<style>
  :root{
    --brand-red:#e2231a;
    --brand-black:#111111;
    --wrap-white:#ffffff;
    --canvas:#ecebe8;
    --panel-edge:#c9c7c3;
    --sky-top:#6f7fae;
    --sky-mid:#c48a8a;
    --sky-low:#e59a55;
    --ground:#3a2f25;
    --hivis:#e9742a;
    --site-grey:#9aa3a8;
  }
  html,body{margin:0;padding:0;width:1200px;height:816px;overflow:hidden;background:var(--canvas);}
  body{font-family:"Archivo",Arial,sans-serif;}
  .layout-board{
    display:grid;grid-template-columns:1fr 1fr;grid-template-rows:1fr 1fr;
    width:1200px;height:816px;box-sizing:border-box;padding:34px 47px;gap:40px 58px;
  }
  .layout-view{display:flex;align-items:center;justify-content:center;}
  .tailgate-panel{width:490px;height:177px;}
  .side-panel{width:500px;height:150px;}
  .lid-panel{width:250px;height:300px;}
  svg text{font-family:"Archivo",Arial,sans-serif;}
  .wordmark{font-weight:800;letter-spacing:-2px;}
  .label{font-weight:600;}
  .body{font-weight:400;}
</style>
</head>
<body>
<main class="layout-board">

  <!-- Tailgate -->
  <section class="layout-view view-rear">
    <svg class="tailgate-panel" viewBox="0 0 525 190" aria-label="Tailgate wrap">
      <rect x="1" y="1" width="523" height="188" fill="var(--wrap-white)" stroke="var(--panel-edge)"/>
      <text class="wordmark" x="14" y="96" font-size="80" fill="var(--brand-black)">TAV</text>
      <circle cx="182" cy="70" r="15" fill="var(--brand-red)"/>
      <text class="label" x="16" y="120" font-size="16" fill="var(--brand-black)">SURVEYORS</text>
      <text class="label" x="14" y="143" font-size="15.5" fill="var(--brand-black)">The Land Measurement &amp;</text>
      <text class="label" x="14" y="163" font-size="15.5" fill="var(--brand-black)">3D Site Scanning Experts.</text>
      <g class="phone-icon" transform="translate(265,96)">
        <circle r="8" fill="var(--brand-red)"/>
        <path d="M-3.5 -4 L-1.5 -4 L-0.5 -1.5 L-2 -0.5 Q-0.5 2 1.5 2.5 L2.5 1 L4.5 2 L4.5 4 Q-4.5 4 -3.5 -4Z" fill="#fff"/>
      </g>
      <text class="label" x="200" y="130" font-size="24" fill="var(--brand-black)">02 5550 0173</text>
      <rect x="250" y="140" width="268" height="42" fill="var(--brand-red)"/>
      <text class="label" x="258" y="158" font-size="15" fill="#fff" textLength="252">www.tavsurveyors-example.com.au</text>
      <text class="label" x="258" y="176" font-size="15" fill="#fff" textLength="252">tav@tavsurveyors-example.com.au</text>
    </svg>
  </section>

  <!-- Driver side (vehicle facing left, tail right) -->
  <section class="layout-view view-side-right">
    <svg class="side-panel" viewBox="0 0 600 180" aria-label="Driver side rear half wrap">
      <defs>
        <linearGradient id="sunsetSky" x1="0" y1="0" x2="0" y2="1">
          <stop offset="0" stop-color="var(--sky-top)"/>
          <stop offset="0.45" stop-color="var(--sky-mid)"/>
          <stop offset="0.72" stop-color="var(--sky-low)"/>
          <stop offset="1" stop-color="var(--ground)"/>
        </linearGradient>
      </defs>
      <rect x="0" y="0" width="600" height="180" fill="var(--wrap-white)" stroke="var(--panel-edge)"/>
      <polygon points="185,0 455,0 425,180 185,180" fill="url(#sunsetSky)" role="img" aria-label="Photo of a survey drone flying over open country at sunset"/>
      <line x1="455" y1="0" x2="425" y2="180" stroke="var(--brand-red)" stroke-width="5"/>
      <path d="M30 180 Q22 70 145 40 L168 0 L185 0 L185 180Z" fill="var(--brand-red)"/>
      <path d="M42 180 Q34 78 150 48 L173 0 L185 0 L185 180Z" fill="var(--brand-black)"/>
      <text class="wordmark" x="66" y="110" font-size="46" fill="#fff">TAV</text>
      <circle cx="166" cy="95" r="9" fill="var(--brand-red)"/>
      <text class="label" x="68" y="124" font-size="10" fill="#fff">SURVEYORS</text>
      <circle cx="70" cy="147" r="9" fill="none" stroke="#fff" stroke-width="2"/>
      <text class="label" x="84" y="151" font-size="16" fill="#fff">02 5550 0173</text>
      <text class="body" x="84" y="160" font-size="6" fill="#fff">www.tavsurveyors-example.com.au</text>
      <text class="body" x="84" y="167" font-size="6" fill="#fff">tav@tavsurveyors-example.com.au</text>
      <text class="wordmark" x="468" y="72" font-size="50" fill="var(--brand-black)">TAV</text>
      <circle cx="578" cy="56" r="10" fill="var(--brand-red)"/>
      <text class="label" x="470" y="88" font-size="11" fill="var(--brand-black)">SURVEYORS</text>
      <text class="body" x="478" y="100" font-size="7" fill="var(--brand-black)">The Land Measurement &amp;</text>
      <text class="body" x="478" y="109" font-size="7" fill="var(--brand-black)">3D Site Scanning Experts.</text>
    </svg>
  </section>

  <!-- Tray lid (top view) -->
  <section class="layout-view view-lid">
    <svg class="lid-panel" viewBox="0 0 240 290" aria-label="Tray lid wrap, top view">
      <rect x="1" y="1" width="238" height="288" rx="8" fill="var(--wrap-white)" stroke="var(--panel-edge)"/>
      <rect x="14" y="14" width="212" height="262" fill="none" stroke="var(--brand-black)" stroke-width="4"/>
      <g transform="translate(0,275) rotate(-90)">
        <text class="wordmark" x="16" y="96" font-size="80" fill="var(--brand-black)">TAV</text>
        <circle cx="186" cy="68" r="14" fill="var(--brand-red)"/>
        <text class="label" x="16" y="117" font-size="18" fill="var(--brand-black)">SURVEYORS</text>
        <text class="label" x="16" y="140" font-size="15" fill="var(--brand-black)">The Land Measurement &amp;</text>
        <text class="label" x="16" y="160" font-size="15" fill="var(--brand-black)">3D Site Scanning Experts.</text>
        <rect x="10" y="173" width="238" height="36" fill="var(--brand-red)"/>
        <circle cx="28" cy="191" r="10" fill="none" stroke="#fff" stroke-width="2.5"/>
        <text class="label" x="46" y="201" font-size="27" fill="#fff">02 5550 0173</text>
      </g>
    </svg>
  </section>

  <!-- Passenger side (vehicle facing right, tail left) -->
  <section class="layout-view view-side-left">
    <svg class="side-panel" viewBox="0 0 600 180" aria-label="Passenger side rear half wrap">
      <defs>
        <linearGradient id="siteScene" x1="0" y1="0" x2="1" y2="0">
          <stop offset="0" stop-color="var(--site-grey)"/>
          <stop offset="0.55" stop-color="#c9cdd0"/>
          <stop offset="1" stop-color="var(--hivis)"/>
        </linearGradient>
      </defs>
      <rect x="0" y="0" width="600" height="180" fill="var(--wrap-white)" stroke="var(--panel-edge)"/>
      <polygon points="145,0 415,0 415,180 175,180" fill="url(#siteScene)" role="img" aria-label="Photo of a surveyor in hi-vis clothing operating survey equipment on site"/>
      <line x1="145" y1="0" x2="175" y2="180" stroke="var(--brand-red)" stroke-width="5"/>
      <path d="M570 180 Q578 70 455 40 L432 0 L415 0 L415 180Z" fill="var(--brand-red)"/>
      <path d="M558 180 Q566 78 450 48 L427 0 L415 0 L415 180Z" fill="var(--brand-black)"/>
      <text class="wordmark" x="420" y="110" font-size="46" fill="#fff">TAV</text>
      <circle cx="520" cy="95" r="9" fill="var(--brand-red)"/>
      <text class="label" x="422" y="124" font-size="10" fill="#fff">SURVEYORS</text>
      <circle cx="428" cy="147" r="9" fill="none" stroke="#fff" stroke-width="2"/>
      <text class="label" x="442" y="151" font-size="16" fill="#fff">02 5550 0173</text>
      <text class="body" x="442" y="160" font-size="6" fill="#fff">www.tavsurveyors-example.com.au</text>
      <text class="body" x="442" y="167" font-size="6" fill="#fff">tav@tavsurveyors-example.com.au</text>
      <text class="wordmark" x="20" y="72" font-size="50" fill="var(--brand-black)">TAV</text>
      <circle cx="130" cy="56" r="10" fill="var(--brand-red)"/>
      <text class="label" x="22" y="88" font-size="11" fill="var(--brand-black)">SURVEYORS</text>
      <text class="body" x="22" y="100" font-size="7" fill="var(--brand-black)">The Land Measurement &amp;</text>
      <text class="body" x="22" y="109" font-size="7" fill="var(--brand-black)">3D Site Scanning Experts.</text>
    </svg>
  </section>

</main>
</body>
</html>
```